card design for engineering consultancy

engineering drafting and project management company the provides drafting services for.
Electrical, Hydraulic, Mechanical, and Civil services
The company is called K7R Services and logo is as attached
Information on card should be.
1. Logo
2.website : K7RServices.com
3. email : info@K7RServices.com
4. Phone: (+61) 400512738
5. Motto: Design - Document - Develop - Deliver

this card should be basically used for business identification only

Target Market(s)

electricians plumbers air conditioning installers and civil contractors

Industry/Entity Type

engineering, drafting, electrical, plumbing, airconditioning, civil

Contact Information for Business Card

1. Logo 2.website : K7RServices.com 3. email : info@K7RServices.com 4. Phone: (+61) 400512738 5. Motto: Design - Document - Develop - Deliver

Font styles to use
Serif

Requirements
Must have
• logo
Nice to have
• something inovative and different that makes it stand out from being just another business card

```html
<!DOCTYPE html>
<html lang="en">
<head>
<meta charset="utf-8">
<title>K7R Services – Business Card</title>
<link rel="stylesheet" href="https://fonts.googleapis.com/css2?family=Noto+Serif:wght@400;700&display=swap">
<style>
  :root {
    --brand-red: #cf2027;
    --brand-grey: #535050;
    --ink: #2e2e2e;
    --card: #ffffff;
    --page: #f1f1f1;
  }
  * { box-sizing: border-box; margin: 0; padding: 0; }
  html, body { width: 1200px; height: 896px; overflow: hidden; }
  body {
    background: var(--page);
    font-family: "Noto Serif", Georgia, serif;
    color: var(--ink);
    position: relative;
  }
  .card {
    position: absolute;
    left: 334px;
    width: 527px;
    height: 302px;
    background: var(--card);
    border-radius: 29px;
  }
  .card--front { top: 125px; }
  .card--back  { top: 471px; }

  .wordmark {
    position: absolute;
    display: flex;
    align-items: center;
    color: var(--brand-grey);
    font-weight: 700;
    white-space: nowrap;
  }
  .wordmark__square {
    background: var(--brand-red);
    flex: none;
  }
  .card--front .wordmark {
    left: 70px; top: 132px;
    font-size: 25px;
    gap: 10px;
  }
  .card--front .wordmark__square { width: 22px; height: 22px; }
  .card--back .wordmark {
    left: 0; right: 0; top: 0; bottom: 0;
    justify-content: center;
    font-size: 52px;
    gap: 18px;
  }
  .card--back .wordmark__square { width: 44px; height: 44px; }

  .details {
    position: absolute;
    left: 289px; top: 70px;
    height: 162px;
    border-left: 1.5px solid var(--brand-red);
    padding-left: 10px;
  }
  .details__name {
    color: var(--brand-red);
    font-size: 20px;
    font-weight: 700;
    line-height: 1;
    margin-top: -1px;
  }
  .details__role {
    font-size: 12.5px;
    margin-top: 4px;
  }
  .details__motto {
    font-size: 12.5px;
    line-height: 20px;
    margin-top: 16px;
  }
  .contact-list {
    list-style: none;
    margin-top: 11px;
    font-size: 12.5px;
  }
  .contact-list li {
    display: flex;
    align-items: center;
    gap: 7px;
    height: 20px;
  }
  .contact-list svg { width: 11px; height: 11px; flex: none; fill: var(--brand-red); }
</style>
</head>
<body>

<section class="card card--front">
  <div class="wordmark"><span class="wordmark__square"></span>K7R Services</div>

  <div class="details">
    <h1 class="details__name">MARTIN HALE</h1>
    <p class="details__role">Managing Director</p>
    <p class="details__motto">Motto: Design - Document<br>- Develop - Deliver</p>
    <ul class="contact-list">
      <li>
        <svg viewBox="0 0 24 24" aria-hidden="true"><path d="M6.6 10.8a15 15 0 0 0 6.6 6.6l2.2-2.2a1 1 0 0 1 1-.25 11.4 11.4 0 0 0 3.6.57 1 1 0 0 1 1 1V20a1 1 0 0 1-1 1A17 17 0 0 1 3 4a1 1 0 0 1 1-1h3.5a1 1 0 0 1 1 1c0 1.25.2 2.45.57 3.57a1 1 0 0 1-.25 1z"/></svg>
        (+61) 400512738
      </li>
      <li>
        <svg viewBox="0 0 24 24" aria-hidden="true"><path d="M2 5h20v2l-10 6L2 7z"/><path d="M2 9l10 6 10-6v10H2z"/></svg>
        info@K7RServices.com
      </li>
      <li>
        <svg viewBox="0 0 24 24" aria-hidden="true"><path d="M12 2a10 10 0 1 0 0 20 10 10 0 0 0 0-20zm-1 17.9A8 8 0 0 1 4 12l5 5v1a2 2 0 0 0 2 2zm6.9-2.5A2 2 0 0 0 16 16h-1v-3a1 1 0 0 0-1-1H8v-2h2a1 1 0 0 0 1-1V7h2a2 2 0 0 0 2-2v-.4a8 8 0 0 1 2.9 12.8z"/></svg>
        K7RServices.com
      </li>
    </ul>
  </div>
</section>

<section class="card card--back">
  <div class="wordmark"><span class="wordmark__square"></span>K7R Services</div>
</section>

</body>
</html>
```